Digital Imaging Website Design Project

This project is for 3 page designs - The main Home page design, department page design & content page design which will utilize most of the home page components.

Client Background - http://www.kelrofab.com

An almost Forty year old established printing company that has a large client base of architect/engineering, as the print shop opened up as a blueprinting company, and over the years has grown, changed and expanded to offer document and digital file management for this industry. KRFab. has also always offered color printing services, but recently has expanded their color department to be able to offer amazing dimensional printing, and extreme cutting technology.

These new products and services will be targeted to new industries for repeatable printing needs, promotional, point of purchase color printing, as well as in-store, interior decor/wall. These new printing services are only offered by KRFAB in their area, and they want to convey that they are on the leading edge of color printing technology, while at the same time, not eliminating their existing primary business scaring away their traditional client base of architectural/engineering firms that use them for large format printing, scanning and document management services.

1 - Home Page Design
Primary Goals of the design:

1.Provide a new, eye catching engaging website that conveys the above expansion/growth/cutting edge company.
2.Full screen design please to move away from the 'center' bordered up website they currently have.
3.Design Components – We don't have any media to provide you with exception of our logo. We're looking for fresh design that is exciting and engaging imagery. Additionally, we are working on a color/effected version of our logo to place on the color division page, and this will probably tie in with the design you create for us.
4.It should be designed to be able to work as a responsive design as well so that when installed, will work across devices etc..
5.Colors – Same color scheme, but if you have an accent color you'd like to use to make the site pop, go for it!

Requirements:
1.The 4 divisions of the company should be the main feature so that the client depending on which department they are needing, will see those 4 choices clearly in the design, and they'll know to click on one of them to get more information and to their needed services.

2.The main goal of the site is to get visitors to place an order, there should be a feature on the home page for this call to action.

3.Put in an element that communicates the main benefit of KRFab. - an area for a 1-line Statement/Call to Action / Overall Company Benefit/

4.The 4 divisions need to have eye catching elements related to their products and services, and that clearly illustrate that the user should click on that to go to the appropriate area for products and services

Reprographics
This department is specifically geared to architect/engineering industry
BYLine for optional Use: Partnering with Building Industry Providers since 1975
Related pages for better understanding:
http://www.kelrofab.com/services/portland_professional_printing_services
http://www.kelrofab.com/services/reprographics
Digital File Management
This department is related to Architect/engineers, but can also apply to any other industry needing electronic document management, scanning, or archival services.
BYLine for optional use: Effective & Efficient Digital Solutions at every level.
Related Pages:
http://www.kelrofab.com/colorgraphics/electronic_file_document_management
http://www.kelrofab.com/colorgraphics/document_scanning_service
http://www.kelrofab.com/services/scanning_and_archiving

Color Graphics
This Department is newly expanded / has expanded services / they are focusing more of their efforts on this department and is a key reason for updated website design.
This Department image/representation should be stellar in the imagery to convey the excellence of the color department the services availble.
One of their newest products/services is dimensional printing – not 3-D, but raised element printing. Essentially a client could pick components on their graphic that that they want to 'bump' out, and additional layers would be put in place to create a popped out, dimensional effect. * Bonus points for creating the color department image that effectively conveys this new service – whether it's showing an abstract image/element that is actually raised off the page/paper/component. Additionally the color dimensional printing can be done on practically any material – glass, vinyl, material etc.... Please let me know if you have any questions on this.
BYLine for optional Use: See How Our Color Stands Out From the Rest
Related pages:
http://www.kelrofab.com/colorgraphics
http://www.kelrofab.com/colorgraphics/color_digital_imaging

Equipment & Supplies
This department provides specific supplies and hardware vs. printing products/services. Our largest client base is architects/engineers, but is not limited to this industry. Typical equipment is large printers, and supplies are typically paper products geared to the large format printing services, for the architect/engineers industry.
Byline for optional Use: In-House Printing & Fulfillment Services
Related pages:
http://www.kelrofab.com/varlen_tusk_equipment_sales
http://www.kelrofab.com/supplies

Additionally - Possibly have descriptive text sections below these 4 elements, but this is optional.

2.) Department/Division Page design -

This page should pull the home page element to over based on which division is selected.
Have a submenu design incorporated so that users can navigate to all the products and services that will be listed under that division
Contain a plugin design for FAQs – so that depending on which division page they are on, the appropriate FAQ's would display for use to have easy access to.
Contain a plugin design for – Contact Us easy form – short form –
Name
Company
Number
Email
Project Details/Questions: Text box

3.)Content Page design
This page should have main area for content
Area for an image with slideshow of other supporting images
Optional area for video – most (99%) of the pages will not have videos, but in the case we do, would like an area that will display videos effectively.
Optional FAQ plugin display
Contact plugin display

Global Elements:

Static and very visible site features that are in a position so that if user clicks beyond home page will still see these are:
Get a Quote
Place Order
Digital Plan-room
Call Today - 503-481-7962

Other global components:
SM Icons – QN, Chirpo, WorkLoop
Rotating Testimonial

Navigational Menu:
The KRF Difference
About
Sustainability
Products & Services
Reprograhics
Digital File Management
Color Graphics
Equipment & Supplies
Login
Blog
Contact Us

After the contest – What would be great to have is when a user clicks on one of the departments, it takes that visual element and continues onto it's department page for a smaller but related image - But this may be an after this web design contest.

Additionally will need some other design work on the interior pages, as well, so hoping to find a great designer to complete the other tasks – as well as be the go-to for future endeavors!

Thanks for looking at the project, and I look forward to any questions you may have.
Updates

Looking forward to hearing from interested designers! - If you're curious about my work, you can find my profile at:  https://www.gigmarla.com/users/~07b3e2f95d18c4a260

Target Market(s)

Please see description

Industry/Entity Type

Electronic

Requirements
Must have
• Please see description

```html
<!DOCTYPE html>
<html lang="en">
<head>
<meta charset="utf-8">
<title>Kelro Fabrication — Digital Imaging</title>
<link href="https://fonts.googleapis.com/css2?family=Open+Sans:ital,wght@0,400;0,600;0,700;1,400;1,600&family=PT+Sans+Narrow:wght@700&display=swap" rel="stylesheet">
<style>
:root{
  --navy:#1b2a7a;
  --nav-top:#1f4fb0;
  --nav-bottom:#0d2a82;
  --accent:#1a8fe3;
  --text:#333;
  --caption:rgba(20,20,20,.82);
  --foot-top:#1447a8;
  --foot-bottom:#16206a;
  --foot-line:rgba(255,255,255,.35);
  --band:#efefef;
}
*{box-sizing:border-box;margin:0;padding:0}
html,body{width:1156px;height:1200px;overflow:hidden}
body{font-family:"Open Sans",sans-serif;color:var(--text);background:#fff;position:relative}
a{color:inherit;text-decoration:none}
.wrap{width:868px;margin-left:144px;position:relative}

.site-header{height:81px;background:linear-gradient(#f7f7f7,#fff)}
.brand{position:absolute;left:0;top:20px;display:flex;align-items:center;gap:8px;color:var(--navy);font-weight:700;font-size:32px;letter-spacing:-.5px}
.brand-dot{width:14px;height:14px;border-radius:50%;background:var(--navy)}
.util-links{position:absolute;right:0;top:6px;font-size:10px;color:#333;white-space:nowrap}
.util-links span{margin:0 6px;color:#666}
.call{position:absolute;right:0;top:33px;display:flex;align-items:center;gap:6px;color:var(--accent);font-weight:700;font-size:22px;white-space:nowrap}

.main-nav{height:41px;background:linear-gradient(var(--nav-top),var(--nav-bottom));box-shadow:0 2px 3px rgba(0,0,0,.3)}
.main-nav ul{list-style:none;display:flex;height:41px;align-items:center}
.main-nav li{font-family:"PT Sans Narrow",sans-serif;font-weight:700;color:#fff;font-size:12.6px;white-space:nowrap;text-align:center;border-left:1px solid rgba(255,255,255,.2);line-height:28px}
.main-nav li:last-child{border-right:1px solid rgba(255,255,255,.2)}
.nav-difference{width:142px}
.nav-products{width:149px}
.nav-repro{width:114px}
.nav-digital{width:177px}
.nav-color{width:124px}
.nav-equipment{width:158px}

.divisions{display:flex;height:362px;margin-top:2px}
.division{flex:1;position:relative}
.division .photo{position:absolute;inset:0}
.division .caption{position:absolute;left:0;right:0;bottom:0;height:45px;background:var(--caption);color:#fff;font-size:19px;display:flex;align-items:center;justify-content:center;white-space:nowrap}
.p-repro{background:linear-gradient(135deg,#5b5f63,#dcdcdc 60%,#f4f4f4)}
.p-digital{background:linear-gradient(90deg,#b32b2b,#d8d8d8 45%,#3b4752 80%,#9aa1a8)}
.p-color{background:linear-gradient(160deg,#f5b400,#e83a5a 40%,#8a3fc0 70%,#2a7fe0)}
.p-equip{background:linear-gradient(180deg,#b7c7d8,#e6ebf0 45%,#c9ced3)}

.welcome{padding-top:55px;height:408px;background:linear-gradient(#f1f1f1,#fff 40px)}
.welcome h1{font-weight:400;font-size:23px;color:var(--navy);margin-bottom:12px}
.welcome p{font-size:11.7px;line-height:18px;margin-bottom:18px;width:862px}

.actions{position:absolute;top:772px;left:0;width:1156px;height:131px;background:var(--band);border-top:1px solid #ddd}
.actions .wrap{display:flex;height:100%;padding:24px 0 20px}
.action{flex:1;text-align:center;color:var(--accent);font-size:19px;border-left:1px solid #e0e0e0;border-right:1px solid #fafafa}
.action svg{display:block;margin:0 auto 8px}

.site-footer{position:absolute;top:903px;left:0;width:1156px;height:297px;background:linear-gradient(var(--foot-top),var(--foot-bottom));color:#fff;box-shadow:inset 0 4px 6px rgba(0,0,0,.25)}
.site-footer .wrap{display:flex;padding-top:58px}
.site-footer h3{font-family:"PT Sans Narrow",sans-serif;font-size:13px;margin-bottom:14px}
.sitemap{width:302px}
.sitemap .cols{display:flex;gap:9px}
.list{list-style:none;width:127px;border-top:1px solid var(--foot-line)}
.list li,.contact li{font-size:10.4px;height:24.4px;line-height:24px;border-bottom:1px solid var(--foot-line);white-space:nowrap}
.company{width:263px}
.contact{list-style:none;border-top:1px solid var(--foot-line)}
.social{display:inline-flex;gap:4px;vertical-align:middle;margin-left:3px}
.social i{width:13px;height:13px;background:#fff;display:inline-block;border-radius:2px}
.testimonials{width:265px;margin-left:39px;position:relative}
.testimonials .mark{position:absolute;left:0;top:28px;font-size:44px;color:rgba(255,255,255,.35);font-family:Georgia,serif;line-height:1}
.testimonials blockquote{font-style:italic;font-size:9.9px;line-height:17.2px;padding-left:9px;margin-top:4px;letter-spacing:-.1px}
.testimonials cite{display:block;text-align:right;font-weight:600;font-size:10px;margin-top:8px;white-space:nowrap}
</style>
</head>
<body>
<header class="site-header">
  <div class="wrap">
    <div class="brand"><span class="brand-dot"></span>KRFab.</div>
    <div class="util-links">About<span>/</span>Sustainability<span>/</span>Login<span>/</span>Blog<span>/</span>Contact Us</div>
    <div class="call">
      <svg width="40" height="32" viewBox="0 0 40 32" aria-hidden="true"><path d="M4 10c4-6 28-6 32 0l-4 5-6-3v-3c-4-1-8-1-12 0v3l-6 3z" fill="var(--nav-bottom)"/><rect x="9" y="14" width="22" height="15" rx="3" fill="var(--accent)"/><circle cx="20" cy="21" r="4" fill="#fff"/></svg>
      503-481-7962
    </div>
  </div>
</header>

<nav class="main-nav">
  <div class="wrap">
    <ul>
      <li class="nav-difference">THE KRF DIFFERENCE</li><li class="nav-products">PRODUCTS &amp; SERVICES</li><li class="nav-repro">REPROGRAHICS</li><li class="nav-digital">DIGITAL FILE MANAGEMENT</li><li class="nav-color">COLOR GRAPHICS</li><li class="nav-equipment">EQUIPMENT &amp; SUPPLIES</li>
    </ul>
  </div>
</nav>

<section class="divisions">
  <a class="division"><div class="photo p-repro" role="img" aria-label="Large format plotter printing architectural drawings"></div><div class="caption">Reprographics</div></a>
  <a class="division"><div class="photo p-digital" role="img" aria-label="Designer working at dual computer monitors"></div><div class="caption">Digital File Management</div></a>
  <a class="division"><div class="photo p-color" role="img" aria-label="Fanned colour swatch guide"></div><div class="caption">Color Graphics</div></a>
  <a class="division"><div class="photo p-equip" role="img" aria-label="Production printing equipment in a bright office"></div><div class="caption">Equipment &amp; Supplies</div></a>
</section>

<section class="welcome">
  <div class="wrap">
    <h1>Welcome</h1>
    <p>Kelro Fabrication (KRFab.) is a full service reprographics company serving Oregon and Southwest Washington's design and building community. Founded in 1975 by Daniel Versky, we utilize the latest digital technologies to provide a wide range of reprographics and graphic imaging services.</p>
    <p>Our services range from electronic document management, color digital imaging, photocopying, cad plotting, and high-speed large format printing. We have evolved from a "print and deliver" provider to become the leader in information management and production. Our On-Site programs provide staffed and un-staffed production centers at client sites for maximum efficiency and cost recovery. We are authorized resellers for industry leading equipment and supplies for the design and building market.</p>
  </div>
</section>

<section class="actions">
  <div class="wrap">
    <a class="action">
      <svg width="34" height="44" viewBox="0 0 34 44" aria-hidden="true"><path d="M2 2h20l10 10v30H2z" fill="none" stroke="var(--accent)" stroke-width="3.5"/><path d="M22 2v10h10" fill="none" stroke="var(--accent)" stroke-width="3"/><path d="M9 20h16M9 26h16M9 32h16" stroke="var(--accent)" stroke-width="3"/></svg>
      Get a Quote
    </a>
    <a class="action">
      <svg width="46" height="44" viewBox="0 0 46 44" aria-hidden="true"><path d="M14 14l6-12M32 14L26 2" stroke="var(--accent)" stroke-width="3"/><rect x="0" y="14" width="46" height="7" fill="var(--accent)"/><path d="M4 24h38l-4 18H8z" fill="var(--accent)"/></svg>
      Place Order
    </a>
    <a class="action">
      <svg width="46" height="44" viewBox="0 0 46 44" aria-hidden="true"><path d="M3 2h40a2 2 0 0 1 2 2v26a2 2 0 0 1-2 2H18l-8 10v-10H3a2 2 0 0 1-2-2V4a2 2 0 0 1 2-2z" fill="var(--accent)"/><path d="M8 11h30M8 17h30M8 23h20" stroke="#fff" stroke-width="2.5"/></svg>
      Digital Plan-room
    </a>
  </div>
</section>

<footer class="site-footer">
  <div class="wrap">
    <div class="sitemap">
      <h3>SITEMAP</h3>
      <div class="cols">
        <ul class="list"><li>Home</li><li>The KRF Difference</li><li>About</li><li>Sustainability</li><li>Products &amp; Services</li><li>Reprograhics</li></ul>
        <ul class="list"><li>Digital File Management</li><li>Color Graphics</li><li>Equipment &amp; Supplies</li><li>Login</li><li>Blog</li><li>Contact Us</li></ul>
      </div>
    </div>
    <div class="company">
      <h3>KELRO FABRICATION</h3>
      <ul class="contact">
        <li>2870 NW Harlow Ave. Portland , OR 97211</li>
        <li>Phone: 503-481-7962</li>
        <li>Fax: 503-481-7963</li>
        <li>Email: info@kelrofab.com</li>
        <li>Follow us on: <span class="social" aria-label="QN, Chirpo, WorkLoop, RSS"><i></i><i></i><i></i><i></i></span></li>
        <li>©2013 Kelro Fabrication Inc.</li>
      </ul>
    </div>
    <div class="testimonials">
      <h3>TESTIMONIALS</h3>
      <span class="mark">“</span>
      <blockquote>Lorem ipsum dolor sit amet, consectetur adipiscing elit. Fusce congue mollis nulla quis tincidunt. In tempus justo eget orci imperdiet, nec tempus risus eleifend. Duis et elementum lorem, non facilisis est. Curabitur felis leo, accumsan vitae magna eu, gravida interdum enim. Vivamus sit amet turpis sapien. Aenean fringilla porttitor.</blockquote>
      <cite>— Rosa Delling, Tarnwick Outfitters Inc</cite>
    </div>
  </div>
</footer>
</body>
</html>
```